Aerospace Private Equity Firm Needs Website

We need a website for new private equity fund called Corvin Partners. We buy smaller companies in the aerospace and industrial industries. I have attached some information about the firm. An example of a site we like that is a similar business but focused in a different sector is www.tarnowcare.com. www.quillstonefunds.com is a firm that also invests in aerospace companies.

Industry/Entity Type

Equity

Number of Pages Required

1 page

Colors
0555a3
33a6d7
ec1f27

```html
<!DOCTYPE html>
<html lang="en">
<head>
<meta charset="utf-8">
<title>Corvin Partners</title>
<link href="https://fonts.googleapis.com/css2?family=Questrial&family=Lato:wght@400;700&display=swap" rel="stylesheet">
<style>
  :root {
    --brand-blue: #033f8f;
    --brand-red: #d10a12;
    --sky-light: #f6c39a;
    --sky-mid: #e77b45;
    --sky-dark: #2c2550;
    --ink: #1c1c1c;
    --footer-bg: #050505;
    --white: #ffffff;
  }
  * { box-sizing: border-box; margin: 0; padding: 0; }
  html, body { width: 1200px; height: 972px; overflow: hidden; background: var(--white); }
  .page { position: relative; width: 1200px; height: 972px; font-family: "Lato", sans-serif; color: var(--ink); }

  .hero {
    position: absolute; top: 92px; left: 0; width: 1200px; height: 534px; overflow: hidden;
    background: linear-gradient(180deg, var(--sky-light) 0%, #f3a36c 30%, var(--sky-mid) 52%, #8a4a5a 75%, var(--sky-dark) 100%);
  }
  .sectors { position: absolute; top: 342px; left: 0; width: 1200px; }
  .sector { position: absolute; width: 220px; text-align: center; color: var(--white); font-family: "Questrial", sans-serif; font-size: 29px; line-height: 34px; }
  .sector svg { display: block; margin: 0 auto 20px; }
  .sector--aero { left: 325px; top: 0; }
  .sector--industrial { left: 656px; top: 0; }

  .header-shape { position: absolute; top: 0; left: 0; }
  .brand { position: absolute; top: 28px; left: 80px; font-family: "Questrial", sans-serif; font-size: 32px; color: var(--brand-blue); }

  .nav { position: absolute; top: 36px; left: 360px; height: 56px; display: flex; align-items: center; font-family: "Questrial", sans-serif; font-size: 18px; }
  .nav a { color: var(--white); text-decoration: none; padding: 0 14px; border-left: 1px solid #2f6ec4; line-height: 14px; }
  .nav a:first-child { border-left: none; }

  .welcome { position: absolute; top: 668px; left: 0; width: 1200px; text-align: center; font-family: "Questrial", sans-serif; font-weight: 400; font-size: 38px; color: var(--brand-blue); letter-spacing: 1px; }
  .intro { position: absolute; top: 745px; left: 95px; width: 1010px; text-align: center; font-size: 14.6px; line-height: 24px; }
  .btn-more {
    position: absolute; top: 843px; left: 520px; width: 160px; height: 40px; border-radius: 20px;
    background: var(--brand-red); color: var(--white); font-family: "Questrial", sans-serif; font-size: 17px;
    display: flex; align-items: center; padding-left: 19px; text-decoration: none;
  }
  .btn-more .arrow { position: absolute; right: 6px; top: 7px; width: 26px; height: 26px; border-radius: 50%; background: var(--brand-blue); }

  .footer { position: absolute; top: 923px; left: 0; width: 1200px; height: 49px; background: var(--footer-bg); }
  .copyright { position: absolute; left: 80px; top: 15px; color: var(--white); font-weight: 700; font-size: 14.5px; }
  .social { position: absolute; top: 7px; right: 82px; display: flex; gap: 10px; }
  .social span { width: 34px; height: 34px; border-radius: 50%; border: 2px solid #e9e9e9; }
  .social .s1 { background: #3b5aa5; }
  .social .s2 { background: #1e7fc0; }
  .social .s3 { background: #2fa9e1; }
</style>
</head>
<body>
<div class="page">
  <div class="hero" role="img" aria-label="Passenger jet climbing through an orange sunset sky above dark clouds">
    <div class="sectors">
      <div class="sector sector--aero">
        <svg width="76" height="76" viewBox="0 0 76 76" aria-hidden="true">
          <path fill="#fff" d="M70 6c-4-4-10 0-14 4L46 20 12 10 6 16l28 16-12 13-10-2-5 5 12 6 6 12 5-5-2-10 13-12 16 28 6-6-10-34 10-10c4-4 8-10 4-14z"/>
        </svg>
        Aerospace
      </div>
      <div class="sector sector--industrial">
        <svg width="64" height="76" viewBox="0 0 64 80" aria-hidden="true">
          <path fill="none" stroke="#fff" stroke-width="3" d="M8 5c4-3 10 2 22-1"/>
          <path fill="#fff" d="M2 14h10v36l16-10v10l16-10v10l16-10v38H2z"/>
          <rect x="12" y="58" width="7" height="7" fill="#d9784b"/>
          <rect x="26" y="58" width="7" height="7" fill="#d9784b"/>
          <rect x="40" y="58" width="7" height="7" fill="#d9784b"/>
        </svg>
        industrial
      </div>
    </div>
  </div>

  <svg class="header-shape" width="1200" height="108" viewBox="0 0 1200 108" aria-hidden="true">
    <path fill="#033f8f" d="M290 92 C315 62 330 36 365 36 H1200 V92 Z"/>
    <path fill="#ffffff" d="M0 0 H1200 V36 H365 C330 36 318 62 298 84 C286 98 274 104 255 104 H0 Z"/>
    <path fill="none" stroke="#d10a12" stroke-width="2" d="M0 104 H255 C274 104 286 98 298 84 C318 62 330 36 365 36 H1200"/>
  </svg>
  <div class="brand">Corvin Partners</div>

  <nav class="nav">
    <a href="#">Home</a>
    <a href="#">Team</a>
    <a href="#">Investment Strategy</a>
    <a href="#">Portfolio Companies</a>
    <a href="#">Press Releases</a>
    <a href="#">Contact</a>
  </nav>

  <h1 class="welcome">Welcome To&nbsp; Corvin Partners</h1>
  <p class="intro">Corvin Partners (“Corvin”) is a Los Angeles, California-based private equity firm formed in 2016 by Principals from Larkspur Hill Associates (LHA). Corvin focuses on lower middle-market control investments in aerospace and industrial companies based in North America. The Corvin team has invested successfully in these sectors over a 10-year period while at LHA.</p>
  <a class="btn-more" href="#">READ MORE
    <span class="arrow"><svg width="26" height="26" viewBox="0 0 26 26" aria-hidden="true"><path d="M11 8l5 5-5 5" fill="none" stroke="#fff" stroke-width="2.5"/></svg></span>
  </a>

  <footer class="footer">
    <div class="copyright">Copyright © 2017&nbsp; Corvin Partners.&nbsp;&nbsp; All Rights Reserved.</div>
    <div class="social"><span class="s1"></span><span class="s2"></span><span class="s3"></span></div>
  </footer>
</div>
</body>
</html>
```